Business card design for a real estate company

We need a business card design a real estate development company called "Vantrelo Holding SA" in Switzerland. Space needed for two phone numbers in international format (one is +7 (912) xxx-xx-xx, the other +41 (76) xxx-xx-xx), e-mail (mb@vantrelo.example), name, position and address of the company:
Rue des Tilleuls 24
CH-1700 Fribourg
Switzerland

Target Market(s)

Potential partners, architects, banks etc..

Industry/Entity Type

Business

Requirements
Must have
• Slight, elegant.
Should not have
• Do not include illustrations of buildings etc..

```html
<!DOCTYPE html>
<html lang="en">
<head>
<meta charset="utf-8">
<title>Vantrelo Holding SA – Business Card</title>
<link rel="stylesheet" href="https://fonts.googleapis.com/css2?family=Jost:wght@300;400;500&display=swap">
<style>
  :root {
    --page: #ffffff;
    --card: #000000;
    --ink: #ffffff;
    --accent: #a6cf2a;
    --accent-light: #b9dc3a;
    --accent-deep: #6f8f1c;
  }
  html, body {
    margin: 0;
    padding: 0;
    width: 1200px;
    height: 694px;
    overflow: hidden;
    background: var(--page);
  }
  .canvas {
    position: relative;
    width: 1200px;
    height: 694px;
    background: var(--page);
    font-family: "Jost", "Futura", sans-serif;
  }
  .card {
    position: absolute;
    left: 11px;
    top: 15px;
    width: 1174px;
    height: 664px;
    background: var(--card);
    overflow: hidden;
  }
  .card__accent {
    position: absolute;
    left: 0;
    top: 0;
    width: 435px;
    height: 365px;
  }
  .card__text {
    position: absolute;
    right: 40px;
    margin: 0;
    line-height: 1;
    text-align: right;
    white-space: nowrap;
    text-transform: uppercase;
  }
  .company-name {
    top: 80px;
    font-size: 50px;
    font-weight: 400;
    letter-spacing: 0.5px;
    color: var(--ink);
  }
  .person-name {
    top: 392px;
    font-size: 38px;
    font-weight: 300;
    color: var(--accent);
  }
  .person-position {
    top: 442px;
    font-size: 38px;
    font-weight: 500;
    color: var(--ink);
  }
  .address {
    top: 545px;
    font-size: 31px;
    font-weight: 300;
    color: var(--ink);
  }
  .contacts {
    top: 594px;
    font-size: 31px;
    font-weight: 300;
    color: var(--ink);
  }
  .contacts__phone {
    margin-left: 14px;
  }
  .contacts__email {
    margin-left: 14px;
    font-weight: 500;
    color: var(--accent);
  }
</style>
</head>
<body>
<div class="canvas">
  <div class="card">
    <svg class="card__accent" viewBox="0 0 435 365" role="img" aria-label="Green decorative accent in the top-left corner">
      <defs>
        <linearGradient id="accent-fill" x1="0" y1="0" x2="0" y2="1">
          <stop offset="0" stop-color="var(--accent-light)"/>
          <stop offset="1" stop-color="var(--accent-deep)"/>
        </linearGradient>
      </defs>
      <polygon points="0,0 307,0 435,99 0,365" fill="url(#accent-fill)"/>
    </svg>

    <p class="card__text company-name">Vantrelo Holding SA</p>

    <p class="card__text person-name">First A. Surname</p>
    <p class="card__text person-position">Position</p>

    <p class="card__text address">Rue des Tilleuls 24, CH-1700 Fribourg, Switzerland</p>
    <p class="card__text contacts">
      <span class="contacts__phone">+7 (912) xxx-xx-xx</span>
      <span class="contacts__phone">+41 (76) xxx-xx-xx</span>
      <span class="contacts__email">mb@vantrelo.example</span>
    </p>
  </div>
</div>
</body>
</html>
```